Keys to a Successful Retirement

We have an audience of 175 who will be viewing these slides. They are designed to be "visual aids" to the presentation -- not a hand out. I am uploading the power point that I did --- we want a professional look but want to keep the words on the slides as they are. We want to keep the civic ledger logo we pasted and the Brantford logo, (our firm). Other than that, feel free to swap out pictures if you have better ones. We want to remain in Power Point so that we can edit it as necessary and display using our existing computers.

```html
<!DOCTYPE html>
<html lang="en">
<head>
<meta charset="utf-8">
<title>Brantford Financial Group – Presentation Template</title>
<link rel="stylesheet" href="https://fonts.googleapis.com/css2?family=Figtree:wght@400;600;700;800&display=swap">
<style>
:root{
  --ink:#000;
  --navy:#0c2f6e;
  --navy-mid:#1d4a96;
  --navy-bright:#1f57a8;
  --band:#c3d3ed;
  --title-light:#c0d0ea;
  --heading:#17427f;
  --text:#333;
  --dark-foot:#2d2d2d;
  --paper:#f4f4f4;
  --table-head:#a9a9a9;
  --table-cat:#d4d4d4;
  --opt1:#1c3f78;
  --opt1-alt:#3a5f95;
  --opt2:#4a4a4a;
  --opt2-alt:#6a6a6a;
  --gold:#d9c79a;
}
*{box-sizing:border-box;margin:0;padding:0}
html,body{width:1061px;height:1200px;overflow:hidden;background:var(--ink)}
body{font-family:"Figtree",Arial,sans-serif;color:var(--text)}
.board{position:absolute;left:0;top:0;width:1000px;height:1131px;transform:scale(1.061);transform-origin:0 0}
.slide{position:absolute;width:488px;height:367px;overflow:hidden}
.col-a{left:8px}.col-b{left:505px}
.row-1{top:8px}.row-2{top:383px;height:365px}.row-3{top:757px}

/* cover slides */
.cover{background:radial-gradient(ellipse at 45% 40%,var(--navy-bright),var(--navy) 85%)}
.cover .top-strip{position:absolute;left:0;top:0;width:100%;height:9px;background:var(--band)}
.cover .band{position:absolute;left:0;top:274px;width:100%;height:46px;background:var(--band)}
.cover .foot{position:absolute;left:0;bottom:0;width:100%;height:47px;background:linear-gradient(90deg,#123a7c,#0f3270)}
.brand{position:absolute;display:flex;flex-direction:column;align-items:center;color:var(--gold);font-weight:600;letter-spacing:1.5px;line-height:1}
.brand .sub{font-size:4.5px;letter-spacing:2px;margin-top:3px;font-weight:400}
.cover .brand{left:28px;top:11px;font-size:16px;color:#d6dff0}
.cover .brand .sub{font-size:5.5px}
.presenter{position:absolute;right:28px;top:9px;text-align:right;color:#fff;font-size:12px;line-height:1.35}
.presenter strong{display:block;font-size:14px;font-weight:700;color:var(--band)}
.title{position:absolute;left:42px;top:50px;line-height:.95}
.title .t1{font-size:44px;font-weight:800;color:var(--title-light);letter-spacing:.5px}
.title .t2{font-size:46px;font-weight:800;color:#fff;letter-spacing:.5px}
.title .sub{font-size:23px;color:#e4ebf7;font-weight:400;margin-top:4px}
.title p{font-size:11.5px;color:#fff;line-height:1.4;margin-top:14px}
.chevron{position:absolute;left:394px;top:60px}
.thanks{position:absolute;right:32px;top:52px;text-align:right;font-size:70px;font-weight:800;line-height:.95}
.thanks .a{color:var(--title-light)}.thanks .b{color:#fff}

/* content slides */
.content{background:linear-gradient(160deg,#fdfdfd,#e6e6e6)}
.content::before{content:"";position:absolute;left:0;top:0;width:100%;height:8px;background:var(--heading)}
.content .foot{position:absolute;left:0;bottom:0;width:100%;height:35px;background:var(--dark-foot);border-top:3px solid var(--heading)}
.content .brand{left:22px;top:9px;font-size:10px}
.nav{position:absolute;right:18px;top:7px;display:flex;align-items:center;gap:6px;color:#eee;font-size:12px}
.nav .btn{width:19px;height:17px;background:var(--navy-bright);display:flex;align-items:center;justify-content:center}
.nav .sep{width:1px;height:20px;background:#888;margin:0 6px}
h2{position:absolute;left:22px;top:20px;font-size:27px;font-weight:700;color:#3a3a3a}
h2 em{font-style:normal;color:var(--heading)}

.about{position:absolute;left:20px;top:66px;right:20px;font-size:13px;line-height:1.4;color:#3a3a3a}
.about p{margin-bottom:10px;text-align:justify}
.about b{color:var(--heading);font-weight:600}

.services{position:absolute;left:40px;top:62px;list-style:none;font-size:17px;line-height:23.5px;color:#333}
.services li::before{content:"";display:inline-block;width:6px;height:6px;background:var(--heading);transform:rotate(45deg);margin:0 12px 2px 0}
.team-photo{position:absolute;left:218px;top:80px;width:244px;height:200px;background:radial-gradient(ellipse at 50% 55%,#4b4e57,#2a2c31 45%,rgba(230,230,230,0) 72%)}

.grid{position:absolute;left:23px;top:68px;width:442px;border-collapse:collapse;font-size:8px}
.grid th{height:24px;font-size:12.5px;font-weight:700}
.grid th.c{background:var(--table-head);color:#333;text-align:center}
.grid th.o1{background:var(--opt1);color:#fff}
.grid th.o2{background:#4a4a4a;color:#fff}
.grid td{height:17px;text-align:center}
.grid td.label{text-align:left;padding-left:28px;background:#fff;color:#444;width:220px}
.grid tr:nth-child(even) td.label{background:#f1f1f1}
.grid td.y{background:var(--opt1);color:#fff;font-size:10px;width:111px}
.grid tr.alt td.y{background:var(--opt1-alt)}
.grid td.n{background:var(--opt2);color:#ddd;width:111px}
.grid tr.alt td.n{background:var(--opt2-alt)}
.grid tr.cat td{background:var(--table-cat);color:#333;font-weight:700;font-size:9.5px;text-align:left;padding-left:4px;height:16px}

.map{position:absolute;left:29px;top:69px;width:209px;height:209px;border:4px solid #fff;box-shadow:0 0 3px rgba(0,0,0,.3);background:linear-gradient(160deg,#cfe0c8 0%,#e2dcc4 40%,#9fc3e6 65%,#d8d2b8 100%)}
.contact{position:absolute;left:254px;top:70px;width:222px;font-size:8.6px;line-height:1.35;color:#444}
.contact .lead{text-align:justify;margin-bottom:6px}
.contact .lead b{color:var(--heading)}
.contact h3{font-size:10.5px;color:var(--heading);font-weight:700;margin-top:6px}
.social{position:absolute;left:34px;top:293px;display:flex;gap:9px;align-items:center;font-size:11px;font-weight:700;color:var(--heading)}
.social .sq{width:17px;height:17px;background:var(--heading)}
</style>
</head>
<body>
<main class="board">

  <section class="slide cover col-a row-1">
    <div class="top-strip"></div>
    <div class="title">
      <div class="t1">TITLE</div>
      <div class="t2">PROJECT</div>
      <div class="sub">subtext presentation</div>
      <p>Lorem ipsum dolor sit amet, consectetuer adipiscing elit.<br>Maecenas porttitor congue massa.</p>
    </div>
    <svg class="chevron" width="58" height="102" viewBox="0 0 58 102"><polygon points="0,0 22,0 58,51 22,102 0,102 34,51" fill="#fff"/></svg>
    <div class="band"></div>
    <footer class="foot">
      <div class="brand">BRANTFORD<span class="sub">FINANCIAL GROUP</span></div>
      <div class="presenter">Presentation by<strong>Daniel Reyes</strong></div>
    </footer>
  </section>

  <section class="slide content col-b row-1">
    <h2><em>About</em> Company</h2>
    <div class="about">
      <p><b>Lorem ipsum</b> dolor sit amet, consectetuer adipiscing elit. Maecenas porttitor congue massa. Fusce posuere, magna sed pulvinar ultricies, purus lectus malesuada libero, sit amet commodo magna eros quis urna.</p>
      <p><b>Nunc viverra imperdiet enim</b>. Fusce est. Vivamus a tellus. Pellentesque habitant morbi tristique senectus et netus et malesuada fames ac turpis egestas. Proin pharetra nonummy pede. Mauris et orci.</p>
      <p><b>Aenean nec lorem</b>. In porttitor. Donec laoreet nonummy augue.</p>
      <p>Suspendisse dui purus, scelerisque at, vulputate vitae, pretium mattis, nunc. Mauris eget neque at sem venenatis eleifend. Ut nonummy.</p>
      <p><b>Fusce aliquet pede non pede</b>.<br>Suspendisse dapibus lorem pellentesque magna. Integer nulla.</p>
    </div>
    <footer class="foot">
      <div class="brand">BRANTFORD<span class="sub">FINANCIAL GROUP</span></div>
      <div class="nav"><span class="btn"><svg width="8" height="10"><polyline points="6,1 2,5 6,9" stroke="#fff" stroke-width="2.2" fill="none"/></svg></span><span class="btn"><svg width="8" height="10"><polyline points="2,1 6,5 2,9" stroke="#fff" stroke-width="2.2" fill="none"/></svg></span><span class="sep"></span>2</div>
    </footer>
  </section>

  <section class="slide content col-a row-2">
    <h2><em>Our</em> Services</h2>
    <ul class="services">
      <li>Lorem ipsum</li><li>Lorem ipsum</li><li>Lorem ipsum</li><li>Lorem ipsum</li><li>Lorem ipsum</li>
      <li>Lorem ipsum</li><li>Lorem ipsum</li><li>Lorem ipsum</li><li>Lorem ipsum</li><li>Lorem ipsum</li>
    </ul>
    <div class="team-photo" role="img" aria-label="Photo of a team of business professionals in suits standing together"></div>
    <footer class="foot">
      <div class="brand">BRANTFORD<span class="sub">FINANCIAL GROUP</span></div>
      <div class="nav"><span class="btn"><svg width="8" height="10"><polyline points="6,1 2,5 6,9" stroke="#fff" stroke-width="2.2" fill="none"/></svg></span><span class="btn"><svg width="8" height="10"><polyline points="2,1 6,5 2,9" stroke="#fff" stroke-width="2.2" fill="none"/></svg></span><span class="sep"></span>3</div>
    </footer>
  </section>

  <section class="slide content col-b row-2">
    <h2><em>Table</em> Presentation</h2>
    <table class="grid">
      <tr><th class="c">CATEGORY</th><th class="o1">OPTION 1</th><th class="o2">OPTION 2</th></tr>
      <tr class="cat"><td colspan="3">Category 1</td></tr>
      <tr><td class="label">Lorem ipsum dolor sit amet</td><td class="y">Yes</td><td class="n">-</td></tr>
      <tr class="alt"><td class="label">Lorem ipsum dolor sit amet</td><td class="y">Yes</td><td class="n">-</td></tr>
      <tr><td class="label">Lorem ipsum dolor sit amet</td><td class="y">Yes</td><td class="n">-</td></tr>
      <tr class="cat"><td colspan="3">Category 2</td></tr>
      <tr><td class="label">Lorem ipsum dolor sit amet</td><td class="y">Yes</td><td class="n">-</td></tr>
      <tr class="alt"><td class="label">Lorem ipsum dolor sit amet</td><td class="y">Yes</td><td class="n">-</td></tr>
      <tr><td class="label">Lorem ipsum dolor sit amet</td><td class="y">Yes</td><td class="n">-</td></tr>
      <tr class="alt"><td class="label">Lorem ipsum dolor sit amet</td><td class="y">Yes</td><td class="n">-</td></tr>
      <tr class="cat"><td colspan="3">Category 3</td></tr>
      <tr><td class="label">Lorem ipsum dolor sit amet</td><td class="y">Yes</td><td class="n">-</td></tr>
      <tr class="alt"><td class="label">Lorem ipsum dolor sit amet</td><td class="y">Yes</td><td class="n">-</td></tr>
    </table>
    <footer class="foot">
      <div class="brand">BRANTFORD<span class="sub">FINANCIAL GROUP</span></div>
      <div class="nav"><span class="btn"><svg width="8" height="10"><polyline points="6,1 2,5 6,9" stroke="#fff" stroke-width="2.2" fill="none"/></svg></span><span class="btn"><svg width="8" height="10"><polyline points="2,1 6,5 2,9" stroke="#fff" stroke-width="2.2" fill="none"/></svg></span><span class="sep"></span>4</div>
    </footer>
  </section>

  <section class="slide content col-a row-3">
    <h2><em>Contact</em> Info</h2>
    <div class="map" role="img" aria-label="Map of the office region"></div>
    <div class="contact">
      <p class="lead"><b>Lorem ipsum</b> dolor sit amet, consectetuer adipiscing elit. Maecenas porttitor congue massa. Fusce posuere, magna sed pulvinar ultricies, purus lectus malesuada libero, sit amet commodo magna eros quis urna.</p>
      <h3>Address</h3>
      <p>1234 Street Address<br>Harbor City, America<br>67890 (U.S.A)</p>
      <h3>Phone</h3><p>0123-456-789</p>
      <h3>FAX</h3><p>0123-456-789</p>
      <h3>Email</h3><p>info@yourcompany.com</p>
      <h3>Website</h3><p>www.yourcompany.com</p>
    </div>
    <div class="social"><span class="sq"></span><span class="sq"></span><span class="sq"></span><span class="sq"></span>@YOURCOMPANY</div>
    <footer class="foot">
      <div class="brand">BRANTFORD<span class="sub">FINANCIAL GROUP</span></div>
      <div class="nav"><span class="btn"><svg width="8" height="10"><polyline points="6,1 2,5 6,9" stroke="#fff" stroke-width="2.2" fill="none"/></svg></span><span class="btn"><svg width="8" height="10"><polyline points="2,1 6,5 2,9" stroke="#fff" stroke-width="2.2" fill="none"/></svg></span><span class="sep"></span>5</div>
    </footer>
  </section>

  <section class="slide cover col-b row-3">
    <div class="top-strip"></div>
    <div class="thanks"><div class="a">Thank</div><div class="b">You</div></div>
    <div class="band"></div>
    <footer class="foot">
      <div class="brand">BRANTFORD<span class="sub">FINANCIAL GROUP</span></div>
      <div class="presenter">Presentation by<strong>Daniel Reyes</strong></div>
    </footer>
  </section>

</main>
</body>
</html>
```